Carpet Cleaning Door Hanger Design Project

please design a door hanger for us. we do carpet cleaning. our company name is Velta Rug Works. our telephone number is 866-402-5719.

please make a special offer coupon.

please add bullets containing the following info-
Professional carpet, hardwood, tile & grout deep steam cleaning.
kid & pet safe.
fast drying.
100% eco friendly / toxin free products.
pet stain/s & odor control.
same day appointments.
clean uniformed employees.
and please put few other catchy lines.

please make a $20.00 of carpet cleaning coupon (restrictions apply).
please make a rooms starting at $59.99 (restrictions apply).

please also put- when you want the best for less call velta rug works.

Target Market(s)

home owners, home renters. new home buyers. new home sellers.

Industry/Entity Type

Home Improvement

Requirements
Must have
• special offer.
• double sided.
• must be a design for a door hanger.
Nice to have
• 100% satisfaction guaranteed bubble.
Should not have
• no website please

```html
<!DOCTYPE html>
<html lang="en">
<head>
<meta charset="utf-8">
<title>Velta Rug Works – Door Hanger</title>
<link href="https://fonts.googleapis.com/css2?family=Archivo+Black&family=Roboto:ital,wght@1,900&family=Oswald:wght@500&family=Open+Sans:wght@700&display=swap" rel="stylesheet">
<style>
  :root{
    --navy:#2e3192;
    --red:#d2352b;
    --purple:#5b2a86;
    --white:#ffffff;
    --backdrop:#dcdcdc;
    --gold:#d9a928;
    --ribbon:#c33a3f;
    --ribbon-fold:#7a1f24;
  }
  html,body{margin:0;padding:0;overflow:hidden;}
  body{width:1200px;height:1200px;background:var(--backdrop);position:relative;}
  .hanger{position:absolute;top:70px;width:460px;height:1060px;filter:drop-shadow(0 6px 10px rgba(0,0,0,.25));}
  .hanger--front{left:100px;}
  .hanger--back{left:640px;}
  .brand{font-family:"Archivo Black",sans-serif;fill:var(--white);}
  .heading{font-family:"Roboto",sans-serif;font-style:italic;font-weight:900;fill:var(--purple);}
  .bullet-text{font-family:"Roboto",sans-serif;font-style:italic;font-weight:900;fill:var(--navy);font-size:16px;}
  .call{font-family:"Roboto",sans-serif;font-style:italic;font-weight:900;fill:var(--navy);}
  .phone{font-family:"Roboto",sans-serif;font-style:italic;font-weight:900;fill:var(--red);}
  .tagline{font-family:"Roboto",sans-serif;font-style:italic;font-weight:900;fill:var(--navy);}
  .ribbon-text{font-family:"Open Sans",sans-serif;font-weight:700;fill:var(--white);}
  .coupon-label{font-family:"Oswald",sans-serif;font-weight:500;fill:#222;font-size:16px;}
  .coupon-price{font-family:"Oswald",sans-serif;font-weight:500;fill:var(--navy);font-size:42px;}
</style>
</head>
<body>

<svg class="hanger hanger--front" viewBox="0 0 460 1060" xmlns="http://www.w3.org/2000/svg">
  <defs>
    <clipPath id="front-edge"><rect width="460" height="1060"/></clipPath>
    <linearGradient id="family-photo" x1="0" y1="0" x2="0" y2="1">
      <stop offset="0" stop-color="#c9c6c2"/>
      <stop offset=".5" stop-color="#b8a79a"/>
      <stop offset="1" stop-color="#d8d6d3"/>
    </linearGradient>
    <linearGradient id="tech-photo" x1="0" y1="0" x2="0" y2="1">
      <stop offset="0" stop-color="#e7e4df"/>
      <stop offset=".55" stop-color="#5a9fc0"/>
      <stop offset="1" stop-color="#8f877c"/>
    </linearGradient>
  </defs>
  <g clip-path="url(#front-edge)">
    <rect class="card" width="460" height="1060" fill="var(--white)"/>
    <rect class="header-band" width="460" height="380" fill="var(--navy)"/>
    <circle class="hang-hole" cx="230" cy="90" r="52" fill="var(--backdrop)"/>
    <text class="brand" x="230" y="222" font-size="48" text-anchor="middle">VELTA RUG</text>
    <text class="brand" x="230" y="280" font-size="48" text-anchor="middle">WORKS</text>

    <polygon class="accent-band" points="0,372 460,346 460,382 0,392" fill="var(--red)"/>
    <rect class="photo" x="0" y="385" width="460" height="185" fill="url(#family-photo)" role="img" aria-label="Smiling family lying on a freshly cleaned carpet"/>
    <polygon class="accent-band" points="0,575 460,548 460,588 0,590" fill="var(--red)"/>
    <polygon class="accent-wedge" points="0,588 200,588 0,615" fill="var(--navy)"/>

    <text class="heading" x="35" y="638" font-size="20">RELIABLE CARPET CLEANING</text>
    <line x1="30" y1="648" x2="430" y2="644" stroke="var(--red)" stroke-width="1.5"/>

    <g class="service-list">
      <g transform="translate(0,674)"><circle cx="32" cy="-6" r="8" fill="none" stroke="var(--navy)" stroke-width="2"/><circle cx="32" cy="-5" r="3.5" fill="var(--red)"/><text class="bullet-text" x="46" y="0">Professional Carpet, Hardwood</text></g>
      <g transform="translate(0,703)"><circle cx="32" cy="-6" r="8" fill="none" stroke="var(--navy)" stroke-width="2"/><circle cx="32" cy="-5" r="3.5" fill="var(--red)"/><text class="bullet-text" x="46" y="0">Tile &amp; Grout Deep Steam Cleaning.</text></g>
      <g transform="translate(0,732)"><circle cx="32" cy="-6" r="8" fill="none" stroke="var(--navy)" stroke-width="2"/><circle cx="32" cy="-5" r="3.5" fill="var(--red)"/><text class="bullet-text" x="46" y="0">Kid &amp; Pet Safe.</text></g>
      <g transform="translate(0,761)"><circle cx="32" cy="-6" r="8" fill="none" stroke="var(--navy)" stroke-width="2"/><circle cx="32" cy="-5" r="3.5" fill="var(--red)"/><text class="bullet-text" x="46" y="0">Fast Drying.</text></g>
      <g transform="translate(0,790)"><circle cx="32" cy="-6" r="8" fill="none" stroke="var(--navy)" stroke-width="2"/><circle cx="32" cy="-5" r="3.5" fill="var(--red)"/><text class="bullet-text" x="46" y="0">100% Eco Friendly / Toxin Free Products.</text></g>
      <g transform="translate(0,819)"><circle cx="32" cy="-6" r="8" fill="none" stroke="var(--navy)" stroke-width="2"/><circle cx="32" cy="-5" r="3.5" fill="var(--red)"/><text class="bullet-text" x="46" y="0">Pet Stand &amp; Odor Control.</text></g>
      <g transform="translate(0,848)"><circle cx="32" cy="-6" r="8" fill="none" stroke="var(--navy)" stroke-width="2"/><circle cx="32" cy="-5" r="3.5" fill="var(--red)"/><text class="bullet-text" x="46" y="0">Same Day Appointments.</text></g>
      <g transform="translate(0,877)"><circle cx="32" cy="-6" r="8" fill="none" stroke="var(--navy)" stroke-width="2"/><circle cx="32" cy="-5" r="3.5" fill="var(--red)"/><text class="bullet-text" x="46" y="0">Clean Uniformed Employees.</text></g>
    </g>

    <circle class="guarantee-seal" cx="95" cy="938" r="44" fill="var(--gold)"/>
    <circle cx="95" cy="938" r="30" fill="#2a2a2a"/>

    <circle class="photo-ring" cx="410" cy="972" r="100" fill="var(--red)"/>
    <circle class="photo" cx="410" cy="972" r="91" fill="url(#tech-photo)" role="img" aria-label="Technician in blue uniform steam cleaning a carpet"/>

    <rect x="0" y="990" width="290" height="5" fill="var(--red)"/>
    <rect class="card" x="0" y="995" width="290" height="55" fill="var(--white)"/>
    <text class="call" x="60" y="1017" font-size="18">CALL US TODAY</text>
    <text class="phone" x="22" y="1045" font-size="30">866-402-5719</text>
    <rect class="footer-band" x="0" y="1050" width="460" height="10" fill="var(--navy)"/>
  </g>
</svg>

<svg class="hanger hanger--back" viewBox="0 0 460 1060" xmlns="http://www.w3.org/2000/svg">
  <defs>
    <clipPath id="back-edge"><rect width="460" height="1060"/></clipPath>
    <linearGradient id="cleaning-photo" x1="0" y1="0" x2="0" y2="1">
      <stop offset="0" stop-color="#ebe7e1"/>
      <stop offset=".4" stop-color="#c9c2b8"/>
      <stop offset="1" stop-color="#8b8378"/>
    </linearGradient>
  </defs>
  <g clip-path="url(#back-edge)">
    <rect class="card" width="460" height="1060" fill="var(--white)"/>
    <polygon class="header-band" points="0,0 460,0 460,418 0,382" fill="var(--navy)"/>
    <polygon class="accent-band" points="0,382 460,418 460,455 0,398" fill="var(--red)"/>
    <circle class="hang-hole" cx="230" cy="95" r="55" fill="var(--backdrop)"/>
    <text class="brand" x="230" y="240" font-size="48" text-anchor="middle">VELTA RUG</text>
    <text class="brand" x="230" y="300" font-size="48" text-anchor="middle">WORKS</text>

    <text class="tagline" x="230" y="500" font-size="27" text-anchor="middle">WHEN YOU WANT THE</text>
    <text class="tagline" x="230" y="534" font-size="27" text-anchor="middle">BEST FOR LESS, CALL</text>
    <text class="tagline" x="230" y="582" font-size="37" text-anchor="middle">VELTA RUG WORKS</text>

    <rect class="photo" x="0" y="605" width="460" height="383" fill="url(#cleaning-photo)" role="img" aria-label="Technician in blue uniform vacuuming a living room carpet"/>
    <polygon class="accent-band" points="150,745 460,770 460,800 150,775" fill="var(--red)"/>

    <g class="offer-ribbon">
      <polygon points="160,612 440,612 440,668 185,668 200,640" fill="var(--ribbon)"/>
      <polygon points="175,668 440,668 420,684 175,684" fill="var(--ribbon-fold)"/>
      <polygon points="170,684 430,684 450,712 430,740 170,740" fill="var(--ribbon)"/>
      <text class="ribbon-text" x="305" y="657" font-size="40" text-anchor="middle">SPECIAL</text>
      <text class="ribbon-text" x="300" y="728" font-size="42" text-anchor="middle">OFFER</text>
    </g>

    <g class="coupon">
      <rect x="200" y="790" width="235" height="86" fill="var(--white)"/>
      <rect x="207" y="797" width="221" height="72" fill="none" stroke="#333" stroke-width="1.3" stroke-dasharray="5 4"/>
      <text class="coupon-label" x="252" y="829" text-anchor="middle">CARPET</text>
      <text class="coupon-label" x="252" y="851" text-anchor="middle">CLEANING</text>
      <line x1="292" y1="806" x2="292" y2="860" stroke="#333" stroke-width="1.3"/>
      <text class="coupon-price" x="362" y="853" text-anchor="middle">$ 20.00</text>
    </g>
    <g class="coupon">
      <rect x="190" y="888" width="235" height="86" fill="var(--white)"/>
      <rect x="197" y="895" width="221" height="72" fill="none" stroke="#333" stroke-width="1.3" stroke-dasharray="5 4"/>
      <text class="coupon-label" x="242" y="927" text-anchor="middle">ROOMS</text>
      <text class="coupon-label" x="242" y="949" text-anchor="middle">CLEANING</text>
      <line x1="282" y1="904" x2="282" y2="958" stroke="#333" stroke-width="1.3"/>
      <text class="coupon-price" x="352" y="951" text-anchor="middle">$ 59.99</text>
    </g>

    <rect x="0" y="988" width="460" height="6" fill="var(--red)"/>
    <text class="call" x="50" y="1017" font-size="19">CALL US TODAY</text>
    <text class="phone" x="30" y="1045" font-size="32">866-402-5719</text>
    <rect class="footer-band" x="0" y="1050" width="460" height="10" fill="var(--navy)"/>
  </g>
</svg>

</body>
</html>
```